Brightmoor Partners Branding Revamp

We are a consulting company, looking for a way to display and promote our brand. We have 2 sides to the business- Brightmoor (financial) and Partners (cyber security). The financial side products relate to business necessities: card processing, website design/hosting/maintenance, VoIP phone systems. The cyber security side promotes a bundled package of 4 solutions: network vulnerability scan, dark web scan, anti-ransomeware/malware software, and image-level backups. We want people to understand that partnering with Brightmoor Partners gives them “Elevated Peace of Mind” (tagline). Current badge and logos uploaded.

Target Market(s)

Small businesses

Contact Information for Business Card

Lena Marwick, Vice President, lena@brightmoorpartners.example, 555-806-1937, www.brightmoorpartners.example

Requirements
Nice to have
• I do prefer the darker background for front and back

```html
<!DOCTYPE html>
<html lang="en">
<head>
<meta charset="utf-8">
<title>Brightmoor Partners — Business Card</title>
<link rel="stylesheet" href="https://fonts.googleapis.com/css2?family=Montserrat:wght@600;800&family=Open+Sans:ital,wght@0,400;1,400&display=swap">
<style>
  :root {
    --backdrop: #1d1d21;
    --card-navy: #100f38;
    --brand-red: #ec1c2b;
    --text-white: #ffffff;
    --card-w: 660px;
    --card-h: 377px;
  }
  * { box-sizing: border-box; margin: 0; padding: 0; }
  html, body {
    width: 1200px;
    height: 900px;
    overflow: hidden;
    background: var(--backdrop);
  }
  .sheet {
    width: 1200px;
    height: 900px;
    display: flex;
    flex-direction: column;
    align-items: center;
    justify-content: center;
    gap: 40px;
  }
  .card {
    width: var(--card-w);
    height: var(--card-h);
    background: var(--card-navy);
    border-radius: 18px;
    position: relative;
    box-shadow: 0 6px 0 var(--brand-red), 0 18px 30px rgba(0,0,0,0.55);
    display: flex;
    align-items: center;
  }
  .wordmark {
    display: flex;
    align-items: center;
    gap: 14px;
    font-family: "Montserrat", sans-serif;
    font-weight: 600;
    color: var(--text-white);
    text-transform: uppercase;
    letter-spacing: 0.32em;
    line-height: 1.35;
  }
  .wordmark-mark {
    width: 22px;
    height: 22px;
    background: var(--brand-red);
    flex: none;
  }
  .card-back { justify-content: center; }
  .card-back .wordmark { font-size: 26px; }
  .card-front { padding: 0 44px; }
  .card-front .wordmark { font-size: 17px; width: 250px; }
  .divider {
    width: 1px;
    height: 150px;
    background: var(--brand-red);
    margin: 0 34px 0 20px;
  }
  .contact { color: var(--text-white); font-family: "Open Sans", sans-serif; }
  .contact-name {
    font-family: "Montserrat", sans-serif;
    font-weight: 800;
    color: var(--brand-red);
    font-size: 25px;
    text-transform: uppercase;
    letter-spacing: 0.01em;
  }
  .contact-title { font-style: italic; font-size: 16px; margin: 2px 0 20px; }
  .contact-list { list-style: none; font-size: 15px; }
  .contact-list li { display: flex; align-items: center; gap: 10px; margin-bottom: 8px; }
  .contact-list svg { width: 15px; height: 15px; flex: none; fill: var(--brand-red); }
</style>
</head>
<body>
<main class="sheet">
  <section class="card card-back" aria-label="Card back">
    <div class="wordmark">
      <span class="wordmark-mark"></span>
      <span>Brightmoor<br>Partners</span>
    </div>
  </section>

  <section class="card card-front" aria-label="Card front">
    <div class="wordmark">
      <span class="wordmark-mark"></span>
      <span>Brightmoor<br>Partners</span>
    </div>
    <div class="divider"></div>
    <div class="contact">
      <h1 class="contact-name">Lena Marwick</h1>
      <p class="contact-title">Vice President</p>
      <ul class="contact-list">
        <li>
          <svg viewBox="0 0 24 24" aria-hidden="true"><path d="M6.6 10.8a15.1 15.1 0 0 0 6.6 6.6l2.2-2.2a1 1 0 0 1 1-.25 11.4 11.4 0 0 0 3.6.57 1 1 0 0 1 1 1V20a1 1 0 0 1-1 1A17 17 0 0 1 3 4a1 1 0 0 1 1-1h3.5a1 1 0 0 1 1 1c0 1.25.2 2.45.57 3.57a1 1 0 0 1-.25 1z"/></svg>
          <span>555-806-1937</span>
        </li>
        <li>
          <svg viewBox="0 0 24 24" aria-hidden="true"><path d="M2 5h20v14H2z M3.5 6.5 12 13l8.5-6.5" stroke="#100f38" stroke-width="1.5"/></svg>
          <span>lena@brightmoorpartners.example</span>
        </li>
        <li>
          <svg viewBox="0 0 24 24" aria-hidden="true"><circle cx="12" cy="12" r="10"/><path d="M2 12h20M12 2c3 3 3 17 0 20M12 2c-3 3-3 17 0 20" stroke="#100f38" stroke-width="1.4" fill="none"/></svg>
          <span>www.brightmoorpartners.example</span>
        </li>
      </ul>
    </div>
  </section>
</main>
</body>
</html>
```